Redesign company trifold brochure

We are rebranding our company in September and looking for a more professional design for our brochure.

What we do - providing interdisciplinary care for those supporting ill, elderly and special needs pets at home following the human hospice model of care - is very novel and our brochure is key in explaining it and our offerings.

We serve dogs and cats. Most of the animals are quite sick, elderly. I have many personal and stock photos we can use in the brochure. Please - no pictures of puppies and/or kittens.

The hard part is fitting the info and message into a clear and concise format.

It must be appealing both to pet owners and vets (who are our primary source of patients through referrals).

It should covey WARMTH, COMPASSION, PROFESSIONALISM, and EXPERTISE.

Please look at our website www.QuillbrookAnimalRest.com for more info

We have until now used maroon and copper for colors - to reflect the "sunset" of the pets life. BUT are now changing to Navy, Teal and White to reflect calm, trust and competence.

We will use the same logo recolored.

Existing brochure and new logo are attached.

PLEASE ask questions!!
Updates

We have a library of stock images you are welcome to use. All have been legally acquired and we have the right to use them. You DO NOT have to use them, just sending along in case you wish to. https://www.filecrate.example/sh/kq4mzrt82vplx/BBQ9Trnz-Pydm3hg7aLwRKfZo?dl=0

Our colors are NAVY, TEAL and WHITE. For your reference, the navy we use is 99/87/44/55 (CMYK) The Teal we use is 76/11/44/0 (CMYK) Thank you!

Designers -- pleaseuse pictures of older pets (no puppies or kittens). Below is a link to stock photos we own that would be appropriate for use in the brochure. https://www.filecrate.example/sh/w472fkdl9rzqx/BBTc5EhtyMPLWGVXsdRoF_3k?dl=0 THANK YOU!

Designers -- I would VERY much like to include a photo of a pet in a wheel chair. I have personal photos as well as (purchased) stock photos for this purpose which can be found at http://lnk.example/QARCS-Pets-in-Wheelchairs Thank you!!

Today is the last day! Many of you have submitted beautiful designs and others are rolling in. I am so appreciative of your time and energy!! Please do not let the deadline pass without YOUR very BEST entry being submitted!! Thank you! - Marisol & All of us at Quillbrook Animal Rest & Comfort Services

Target Market(s)

Pet Owners and Veterinarians

Industry/Entity Type

Pet Care

Font styles to use
Serif

Colors
0455a3
33b8a4
ffffff

Requirements
Must have
• Our logo and information about our services. Pictures of pets. Our contact info. PLEASE NOTE: this is a 2 sided brochure. Please submit both inside and outside.
Should not have
• puppies, kittens - anything off message

```html
<!DOCTYPE html>
<html lang="en">
<head>
<meta charset="utf-8">
<title>Quillbrook Animal Rest &amp; Comfort Services – Trifold Brochure</title>
<link rel="stylesheet" href="https://fonts.googleapis.com/css2?family=Cormorant+Garamond:ital,wght@0,500;1,500;1,600&family=Open+Sans:ital,wght@0,300;0,400;0,600;1,400&display=swap">
<style>
  :root {
    --navy: #1b2a4e;
    --navy-deep: #14203d;
    --teal: #33b8a4;
    --teal-dark: #24907f;
    --white: #ffffff;
    --paper: #fbfcfc;
    --ink: #23395f;
    --rule: #e3e7e8;
    --backdrop: #6e6f70;
    --serif: "Cormorant Garamond", Georgia, serif;
    --sans: "Open Sans", Arial, sans-serif;
  }
  * { box-sizing: border-box; margin: 0; padding: 0; }
  html, body { width: 1200px; height: 900px; overflow: hidden; }
  body { background: var(--backdrop); position: relative; font-family: var(--sans); }

  .brochure {
    position: absolute; left: 90px; top: 50px;
    width: 1020px; height: 800px;
    display: flex;
    box-shadow: 0 10px 30px rgba(0,0,0,.35);
  }
  .panel { position: relative; width: 340px; height: 800px; background: var(--paper); overflow: hidden; }
  .panel + .panel { border-left: 1px solid var(--rule); }
  .panel-art { position: absolute; inset: 0; width: 100%; height: 100%; }

  /* Panel: team & beliefs */
  .team-photo-banner {
    position: absolute; left: 0; top: 0; width: 340px; height: 250px;
    background: linear-gradient(160deg, #5a2a14 0%, #8a4120 45%, #b06a3e 100%);
    clip-path: ellipse(95% 100% at 75% 0%);
  }
  .team-photo-portrait {
    position: absolute; left: 22px; top: 105px; width: 150px; height: 150px;
    border-radius: 50%;
    background: radial-gradient(circle at 45% 40%, #d9a460 0%, #b77a3a 60%, #7a4b22 100%);
    border: 5px solid var(--white);
    box-shadow: 0 0 0 2px var(--teal);
  }
  .team-list {
    position: absolute; left: 38px; top: 285px; width: 290px;
    list-style: none;
    font-style: italic; font-size: 13.5px; line-height: 1.55; color: var(--ink);
  }
  .team-list li { position: relative; padding-left: 16px; }
  .team-list li::before {
    content: ""; position: absolute; left: 0; top: 8px;
    width: 6px; height: 6px; border-radius: 50%; background: var(--navy);
  }
  .beliefs { position: absolute; left: 28px; top: 505px; width: 292px; color: var(--navy); }
  .beliefs-title { font-family: var(--serif); font-style: italic; font-weight: 600; font-size: 32px; line-height: 1; margin-bottom: 10px; }
  .beliefs-list { list-style: none; font-style: italic; font-size: 12.5px; line-height: 1.32; }
  .beliefs-list li { position: relative; padding-left: 24px; margin-bottom: 7px; }
  .beliefs-list li::before { content: "\2192"; position: absolute; left: 0; top: 0; font-style: normal; font-size: 13px; }

  /* Panel: contact */
  .contact { position: absolute; left: 34px; top: 64px; width: 276px; }
  .contact-title { font-family: var(--serif); font-style: italic; font-weight: 600; font-size: 32px; line-height: 1; color: var(--teal-dark); margin-bottom: 14px; }
  .contact-name { font-family: var(--serif); font-weight: 500; font-size: 19px; line-height: 1.15; color: var(--navy); margin-bottom: 30px; }
  .contact-list { list-style: none; font-style: normal; }
  .contact-list li { display: flex; align-items: center; gap: 14px; margin-bottom: 24px; font-size: 13px; line-height: 1.35; color: var(--ink); }
  .contact-icon { flex: none; width: 34px; height: 34px; }
  .contact-note { margin-top: 10px; font-style: italic; font-size: 13px; line-height: 1.4; color: var(--ink); }

  /* Panel: cover */
  .cover-photo {
    position: absolute; left: 0; top: 0; width: 340px; height: 500px;
    background: linear-gradient(110deg, #8a5a3a 0%, #c9bdb2 30%, #f1f1f2 50%, #e7e8ea 75%, #cfd3d8 100%);
  }
  .cover-headline {
    position: absolute; left: 22px; top: 36px; width: 250px;
    font-size: 21px; line-height: 1.5; color: var(--white); font-weight: 300;
  }
  .cover-headline span {
    background: var(--teal); padding: 1px 6px;
    -webkit-box-decoration-break: clone; box-decoration-break: clone;
  }
  .cover-tagline {
    position: absolute; right: 28px; top: 320px; width: 230px; text-align: right;
    font-family: var(--serif); font-style: italic; font-weight: 500; font-size: 30px; line-height: 1.05; color: var(--navy);
  }
  .brand {
    position: absolute; left: 58px; top: 648px;
    display: flex; align-items: center; gap: 12px;
  }
  .brand-mark { width: 26px; height: 26px; border-radius: 50%; background: var(--teal); flex: none; }
  .brand-name { font-family: var(--serif); font-weight: 500; font-size: 20px; line-height: 1.05; color: var(--white); width: 220px; }
</style>
</head>
<body>
  <main class="brochure">

    <section class="panel panel-team">
      <div class="team-photo-banner" role="img" aria-label="Close-up photo of a reddish-brown dog's coat"></div>
      <svg class="panel-art" viewBox="0 0 340 800" aria-hidden="true">
        <path d="M0,505 C70,440 230,415 340,470" fill="none" stroke="var(--teal)" stroke-width="2"/>
        <path d="M0,530 C80,455 240,435 340,490 L340,800 L0,800 Z" fill="var(--teal)"/>
      </svg>
      <div class="team-photo-portrait" role="img" aria-label="Portrait photo of an elderly golden retriever"></div>
      <ul class="team-list">
        <li>Certified Thanatologist</li>
        <li>Interfaith Veterinary Technicians</li>
        <li>Certified Spiritual Advisor</li>
        <li>Certified Small Animal Massage Therapist</li>
        <li>Animal Care Specialists</li>
        <li>Hospice Assistants</li>
        <li>Client Care Coordinator</li>
      </ul>
      <div class="beliefs">
        <h2 class="beliefs-title">We Believe</h2>
        <ul class="beliefs-list">
          <li>That animals are conscious beings, capable of thought, feeling, emotion and choice</li>
          <li>That each animal is an individual with his or her unique needs and wishes</li>
          <li>That all pets deserve to be pain-free</li>
          <li>That an interdisciplinary team is essential to addressing the needs of pets and their families through aging and illness</li>
          <li>That quality of life is subjective, best evaluated by the family who knows and loves the animal</li>
        </ul>
      </div>
    </section>

    <section class="panel panel-contact">
      <address class="contact">
        <h2 class="contact-title">Contact Us</h2>
        <p class="contact-name">Quillbrook Animal Rest &amp; Comfort Services</p>
        <ul class="contact-list">
          <li>
            <svg class="contact-icon" viewBox="0 0 34 34" aria-hidden="true"><circle cx="17" cy="17" r="16" fill="var(--teal)"/><path d="M12 9 l4 0 l1 5 l-2.5 1.5 a10 10 0 0 0 5 5 l1.5 -2.5 l5 1 l0 4 a2 2 0 0 1 -2 2 a15 15 0 0 1 -14 -14 a2 2 0 0 1 2 -2 z" fill="var(--white)"/></svg>
            (555) 014-2290
          </li>
          <li>
            <svg class="contact-icon" viewBox="0 0 34 34" aria-hidden="true"><circle cx="17" cy="17" r="16" fill="var(--teal)"/><rect x="9" y="11" width="16" height="12" rx="1.5" fill="none" stroke="var(--white)" stroke-width="2"/><path d="M9.5 12 l7.5 6 l7.5 -6" fill="none" stroke="var(--white)" stroke-width="2"/></svg>
            care@quillbrookanimalrest.com
          </li>
          <li>
            <svg class="contact-icon" viewBox="0 0 34 34" aria-hidden="true"><circle cx="17" cy="17" r="16" fill="var(--teal)"/><circle cx="17" cy="17" r="8" fill="none" stroke="var(--white)" stroke-width="1.8"/><ellipse cx="17" cy="17" rx="3.5" ry="8" fill="none" stroke="var(--white)" stroke-width="1.5"/><path d="M9 17 h16" stroke="var(--white)" stroke-width="1.5"/></svg>
            www.QuillbrookAnimalRest.com
          </li>
          <li>
            <svg class="contact-icon" viewBox="0 0 34 34" aria-hidden="true"><circle cx="17" cy="17" r="16" fill="var(--teal)"/><path d="M17 26 C12 20 11 17 11 14.5 a6 6 0 0 1 12 0 C23 17 22 20 17 26 z" fill="var(--white)"/><circle cx="17" cy="14.5" r="2.2" fill="var(--teal)"/></svg>
            48 Harrow Lane, Ashford Ridge, MA 01234
          </li>
        </ul>
        <p class="contact-note">Serving families at home, seven days a week</p>
      </address>
      <svg class="panel-art" viewBox="0 0 340 800" aria-hidden="true">
        <path d="M0,720 C120,700 240,690 340,700 L340,800 L0,800 Z" fill="var(--teal)"/>
      </svg>
    </section>

    <section class="panel panel-cover">
      <div class="cover-photo" role="img" aria-label="Photo of a white cat and a brown dog touching noses"></div>
      <svg class="panel-art" viewBox="0 0 340 800" aria-hidden="true">
        <defs>
          <linearGradient id="cover-base" x1="0" y1="0" x2="1" y2="1">
            <stop offset="0" stop-color="var(--teal-dark)"/>
            <stop offset="0.55" stop-color="var(--navy)"/>
            <stop offset="1" stop-color="var(--navy-deep)"/>
          </linearGradient>
        </defs>
        <path d="M0,505 C130,480 260,430 340,385 L340,800 L0,800 Z" fill="var(--teal)"/>
        <path d="M0,535 C140,510 270,460 340,420 L340,800 L0,800 Z" fill="var(--navy)"/>
        <path d="M0,575 C140,550 270,505 340,470 L340,800 L0,800 Z" fill="var(--teal)"/>
        <path d="M0,605 C140,580 270,540 340,505 L340,800 L0,800 Z" fill="url(#cover-base)"/>
        <path d="M0,760 C120,745 250,720 340,690 L340,715 C250,745 120,770 0,785 Z" fill="var(--teal)"/>
      </svg>
      <h1 class="cover-headline"><span>Skilled Home Care for Ill, Elderly and Special Needs Animals</span></h1>
      <p class="cover-tagline">Compassionate Support for Families</p>
      <div class="brand">
        <span class="brand-mark"></span>
        <span class="brand-name">Quillbrook Animal Rest &amp; Comfort Services</span>
      </div>
    </section>

  </main>
</body>
</html>
```